Oven Cleaning Business owner needs business card design

Hi there,
Would like for a business card to be designed for myself, the owner of a professional oven cleaning business on the Sunshine Coast.
Would like it to look sleek, and modern-ish. Bit creative is encouraged too.
Include following:
Name/title: Corin ter Haghe, Owner
Phone number: 1300 482 916
Email: info@hearthshinecrew.com.au
Website: www.hearthshinecrew.com.au

```html
<!DOCTYPE html>
<html lang="en">
<head>
<meta charset="utf-8">
<title>Hearthshine Crew – Business Card</title>
<link rel="stylesheet" href="https://fonts.googleapis.com/css2?family=Exo+2:wght@700&family=Open+Sans:wght@400;600&display=swap">
<style>
  :root {
    --backdrop: #8a8a8c;
    --backdrop-edge: #5e5e60;
    --card-white: #ffffff;
    --card-black: #141414;
    --pattern-dark: #1e1e1e;
    --pattern-light: #2c2c2c;
    --aqua: #19d3e0;
    --ink: #1a1a1a;
    --ink-soft: #3a3a3a;
  }
  * { box-sizing: border-box; margin: 0; padding: 0; }
  html, body { width: 1200px; height: 781px; overflow: hidden; }
  body {
    background: radial-gradient(ellipse at 50% 40%, var(--backdrop) 0%, var(--backdrop-edge) 100%);
    position: relative;
    font-family: "Open Sans", sans-serif;
  }
  .card {
    position: absolute;
    top: 242px;
    width: 520px;
    height: 297px;
    border-radius: 3px;
    box-shadow: 0 14px 30px rgba(0,0,0,.35);
    overflow: hidden;
  }
  .card--front { left: 60px; background: var(--card-white); }
  .card--back { left: 620px; background: var(--card-black); }

  .wordmark {
    display: flex;
    align-items: center;
    gap: 12px;
    font-family: "Exo 2", sans-serif;
    font-weight: 700;
    letter-spacing: 1px;
    text-transform: uppercase;
  }
  .wordmark__dot {
    width: 34px; height: 34px; border-radius: 50%;
    background: var(--aqua);
    flex: none;
  }
  .card--front .wordmark {
    position: absolute;
    top: 34px; right: 40px;
    font-size: 26px;
    color: var(--ink);
  }
  .divider {
    position: absolute;
    left: 40px; right: 40px; top: 112px;
    height: 2px;
    background: var(--aqua);
  }
  .holder { position: absolute; left: 40px; top: 134px; }
  .holder__name {
    font-family: "Exo 2", sans-serif;
    font-weight: 700;
    font-size: 22px;
    color: var(--aqua);
  }
  .holder__title { font-size: 12px; color: var(--ink-soft); margin-top: 2px; }
  .contacts { list-style: none; margin-top: 12px; }
  .contacts li {
    display: flex; align-items: center; gap: 8px;
    font-size: 13px; color: var(--ink); line-height: 20px;
  }
  .contacts svg { width: 11px; height: 11px; fill: var(--aqua); flex: none; }

  .back-pattern {
    position: absolute; inset: 0;
    background: linear-gradient(135deg, var(--pattern-dark) 0%, var(--pattern-light) 100%);
  }
  .card--back .wordmark {
    position: absolute;
    left: 50%; top: 50%;
    transform: translate(-50%, -50%);
    font-size: 28px;
    color: var(--aqua);
    white-space: nowrap;
  }
</style>
</head>
<body>
  <section class="card card--front" aria-label="Business card front">
    <div class="wordmark"><span class="wordmark__dot"></span><span>Hearthshine Crew</span></div>
    <div class="divider"></div>
    <div class="holder">
      <p class="holder__name">Corin ter Haghe</p>
      <p class="holder__title">Owner</p>
      <ul class="contacts">
        <li><svg viewBox="0 0 24 24"><path d="M6.6 10.8a15.1 15.1 0 0 0 6.6 6.6l2.2-2.2c.3-.3.7-.4 1-.2 1.1.4 2.3.6 3.6.6.6 0 1 .4 1 1V20c0 .6-.4 1-1 1A17 17 0 0 1 3 4c0-.6.4-1 1-1h3.5c.6 0 1 .4 1 1 0 1.3.2 2.5.6 3.6.1.3 0 .7-.2 1z"/></svg>1300 482 916</li>
        <li><svg viewBox="0 0 24 24"><path d="M2 5h20v14H2z M2 5l10 8 10-8" /></svg>info@hearthshinecrew.com.au</li>
        <li><svg viewBox="0 0 24 24"><circle cx="12" cy="12" r="10"/></svg>www.hearthshinecrew.com.au</li>
      </ul>
    </div>
  </section>

  <section class="card card--back" aria-label="Business card back">
    <div class="back-pattern" role="img" aria-label="Repeating tonal brand-mark pattern on black"></div>
    <div class="wordmark"><span class="wordmark__dot"></span><span>Hearthshine Crew</span></div>
  </section>
</body>
</html>
```